Business Name: K&T Holdings Cleaning Services - Cleaning business

We need a website to be able to get our services out to the market..
We have just invested over $60,000 in our new van which is capable of doing specialised cleaning services see attached flyer... I will also send through our company logo....We do all types of cleaning from move out cleans, office cleans and have the capability fire flood and restoration services as well
On the flyer it has Gerald as a contact do not use his name only use Martin as a contact
Want some good pictures included
Prefer people to contact me via email rather than calling me.

```html
<!DOCTYPE html>
<html lang="en">
<head>
<meta charset="utf-8">
<title>K&amp;T Holdings Cleaning Services</title>
<link rel="stylesheet" href="https://fonts.googleapis.com/css2?family=Montserrat:wght@400;500;600;700&family=Open+Sans:wght@400;600&display=swap">
<style>
:root{
  --blue-hero:#1f4ccc;
  --blue-hero-light:#2d63e0;
  --blue-deep:#064aa0;
  --blue-card:#0b3f8c;
  --blue-card-dark:#053478;
  --blue-button:#1477f0;
  --blue-link:#3a5fc6;
  --about-text:#5c8ce0;
  --orange:#f08a24;
  --ink:#2b2b2b;
  --muted:#777;
  --pale:#eaf2fd;
  --white:#ffffff;
  --line:#d8dbe0;
  --icon-soft:#9fb6e6;
}
*{box-sizing:border-box;margin:0;padding:0}
html,body{width:1200px;height:2778px;overflow:hidden;background:var(--white)}
body{font-family:"Open Sans",Arial,sans-serif;color:var(--ink);position:relative}
.page{position:absolute;left:78px;top:0;width:1046px;height:2778px}

/* nav */
.site-nav{height:52px;border-top:3px solid var(--blue-deep);display:flex;align-items:center;justify-content:space-between;padding:0 60px 0 92px;background:var(--white)}
.brand-small{font-family:"Montserrat",sans-serif;font-weight:600;font-size:10px;color:var(--orange)}
.menu{display:flex;gap:30px;font-family:"Montserrat",sans-serif;font-size:11px;color:var(--ink)}
.menu .active{color:var(--blue-button)}

/* hero */
.hero{position:relative;height:424px;background:linear-gradient(160deg,var(--blue-hero-light),var(--blue-hero) 60%,#1a42b8);overflow:hidden}
.hero-curve{position:absolute;left:0;bottom:0;width:1046px;height:70px}
.hero-title{position:absolute;left:92px;top:70px;font-family:"Montserrat",sans-serif;font-weight:700;font-size:31px;line-height:37px;color:var(--white);letter-spacing:.5px}
.hero-title .accent{color:#a9c8ff;text-decoration:underline;text-decoration-thickness:2px;text-underline-offset:4px}
.hero-actions{position:absolute;left:92px;top:205px;display:flex;gap:26px}
.btn{font-family:"Montserrat",sans-serif;font-weight:600;font-size:10px;color:var(--white);height:30px;border-radius:15px;display:flex;align-items:center;justify-content:center}
.btn-primary{width:126px;background:var(--blue-button)}
.btn-outline{width:132px;border:2px solid var(--white)}
.hero-brand{position:absolute;left:630px;top:150px;width:320px;text-align:center;font-family:"Montserrat",sans-serif;font-weight:600;font-size:26px;line-height:34px;color:var(--white)}

/* tagline */
.tagline{height:248px;padding-top:48px;text-align:center}
.tagline h2{font-family:"Montserrat",sans-serif;font-weight:500;font-size:37px;line-height:44px;color:var(--orange);letter-spacing:1px}
.tagline .email{margin-top:18px;font-size:17px;color:var(--blue-link)}

/* about */
.about{position:relative;height:545px;overflow:hidden}
.about-photo{position:absolute;inset:0;background:linear-gradient(110deg,#4a4d52 0%,#2e3034 35%,#1c1d20 60%,#35373b 100%)}
.about-shade{position:absolute;left:0;top:0;width:100%;height:315px;background:rgba(0,0,0,.35)}
.about h2{position:relative;text-align:center;padding-top:32px;font-family:"Montserrat",sans-serif;font-weight:500;font-size:37px;color:var(--orange);letter-spacing:1px}
.about-lead{position:relative;width:720px;margin:16px auto 0;text-align:center;font-size:17px;line-height:25px;color:var(--about-text)}
.strength{position:absolute;left:10px;top:300px;width:520px;color:var(--white);text-align:center;font-size:11.5px;line-height:17px}
.strength h3{font-family:"Montserrat",sans-serif;font-weight:700;font-size:16px;color:var(--orange);text-align:left;margin:0 0 10px 185px}
.strength p+p{margin-top:12px}
.machine{position:absolute;left:692px;top:290px;width:206px;height:250px;background:linear-gradient(180deg,#3fc35a,#2a9b45 70%,#5a5d62);border-radius:4px}

/* services */
.services{height:683px;background:var(--blue-deep);padding-top:38px;text-align:center;color:var(--white)}
.services h2{font-family:"Montserrat",sans-serif;font-weight:500;font-size:37px;letter-spacing:1px}
.services .sub{font-size:16px;margin-top:8px}
.service-grid{display:grid;grid-template-columns:repeat(3,250px);column-gap:45px;grid-template-rows:121px 155px 172px;row-gap:20px;margin:38px 0 0 107px}
.service-card{background:var(--blue-card);border-radius:4px;padding-top:20px;display:flex;flex-direction:column;align-items:center}
.service-card.highlight{background:var(--blue-card-dark)}
.service-card svg{width:38px;height:30px;margin-bottom:8px}
.service-card h3{font-family:"Montserrat",sans-serif;font-weight:700;font-size:14px;line-height:17px;width:200px}
.service-card p{font-size:11px;line-height:15px;width:210px;margin-top:6px}

/* clients */
.clients{height:223px;background:var(--pale);padding-top:22px;text-align:center}
.clients h2{font-family:"Montserrat",sans-serif;font-weight:500;font-size:37px;color:var(--orange);letter-spacing:1px}
.client-row{display:flex;width:856px;margin:18px 0 0 97px;background:var(--white)}
.client-box{flex:1;height:102px;border-right:1px solid #e6e9ee;display:flex;align-items:center;justify-content:center;font-family:"Montserrat",sans-serif;font-weight:600;font-size:11px;color:var(--orange)}
.client-box:last-child{border-right:0}

/* contact */
.contact{position:relative;height:540px;padding-top:40px}
.contact h2{text-align:center;font-family:"Montserrat",sans-serif;font-weight:500;font-size:37px;color:var(--orange);letter-spacing:1px}
.contact-form{position:absolute;left:96px;top:100px;width:491px}
.field{border:1px solid var(--line);height:24px;font-size:10px;color:var(--muted);padding:5px 8px;margin-bottom:9px}
.field-pair{display:flex;gap:9px}
.field-pair .field{flex:1}
.field.message{height:86px}
.send{position:absolute;left:200px;top:162px;width:128px;height:26px;border-radius:13px;background:var(--blue-button);color:var(--white);font-size:11px;display:flex;align-items:center;justify-content:center}
.contact-info{position:absolute;left:608px;top:100px;width:400px;font-size:10px;line-height:15px;color:var(--orange)}
.info-line{display:flex;gap:12px;align-items:flex-start;margin-bottom:26px}
.info-line svg{flex:none;width:16px;height:16px}
.map{position:absolute;left:15px;top:305px;width:1020px;height:190px;background:linear-gradient(135deg,#e8ecef,#dfe6df 45%,#eef0f2)}

.site-footer{position:absolute;left:0;top:2728px;width:1046px;height:50px;background:var(--blue-deep);color:var(--white);font-size:10px;display:flex;align-items:center;justify-content:center}
.site-footer b{margin:0 4px}
</style>
</head>
<body>
<div class="page">

  <header class="site-nav">
    <div class="brand-small">K&amp;T Holdings</div>
    <nav class="menu"><span class="active">Home</span><span>About Us</span><span>Services</span><span>CliEnts</span><span>Contact Us</span></nav>
  </header>

  <section class="hero">
    <h1 class="hero-title">HIGH PRESSURE<br><span class="accent">CLEANING</span><br>SERVICES</h1>
    <div class="hero-actions"><span class="btn btn-primary">Get Started</span><span class="btn btn-outline">Our Services</span></div>
    <div class="hero-brand">K&amp;T Holdings<br>Cleaning</div>
    <svg class="hero-curve" viewBox="0 0 1046 70" preserveAspectRatio="none"><path d="M0 50 Q523 0 1046 10 L1046 70 L0 70 Z" fill="#ffffff"/></svg>
  </section>

  <section class="tagline">
    <h2>FOR THE HIGHEST PERFORMANCE<br>AND DURABILITY, CHOOSE US!</h2>
    <p class="email">kth.cleaningservices@mailbox.example</p>
  </section>

  <section class="about">
    <div class="about-photo" role="img" aria-label="Photo of the company cleaning van with its equipment, darkened"></div>
    <div class="about-shade"></div>
    <h2>ABOUT US</h2>
    <p class="about-lead">Whether you need to clean your existing premises or even remove graffiti, our commercial cleaning solutions go above and beyond when it comes to restoring your premises. We have extensive experience and work closely with Councils, Recreational Parks, Real Estate Agents, The Department of Human Services, High profile retail shops and more. If you require specialty cleaning - just as - we're up for a challenge because we only use the best equipment and products.</p>
    <div class="strength">
      <h3>Our Strength</h3>
      <p>Our professional Cobalt 500 Truckmount unit, is one of the most powerful slide-in on the market. This unit has more heat, more vacuum power and more pressure for a superior clean! Triple-source heat and a high-pressure solution pump makes it perfect for hard surface cleaning using higher pressure which is ideal for both large commercial and residential jobs.</p>
      <p>The 500 Truckmount has the Ability to steam clean at higher temperatures thus provides quality results &amp; higher sanitisation rates than normal portable steam or pressure cleaners.</p>
    </div>
    <div class="machine" role="img" aria-label="Photo of the green truckmount cleaning machine"></div>
  </section>

  <section class="services">
    <h2>SERVICES</h2>
    <p class="sub">What we specialise in:</p>
    <div class="service-grid">
      <div class="service-card"><svg viewBox="0 0 38 30"><g fill="none" stroke="#fff" stroke-width="2.5"><rect x="3" y="8" width="20" height="14" rx="2"/><path d="M23 12h7l5 6v4H23z"/><circle cx="10" cy="24" r="3" fill="#0b3f8c"/><circle cx="29" cy="24" r="3" fill="#0b3f8c"/></g></svg><h3>Pressure clean driveways and seals</h3></div>
      <div class="service-card"><svg viewBox="0 0 38 30"><g fill="none" stroke="#fff" stroke-width="2.5"><rect x="3" y="8" width="20" height="14" rx="2"/><path d="M23 12h7l5 6v4H23z"/><circle cx="10" cy="24" r="3" fill="#0b3f8c"/><circle cx="29" cy="24" r="3" fill="#0b3f8c"/></g></svg><h3>Tile and grout clean</h3></div>
      <div class="service-card"><svg viewBox="0 0 38 30"><g fill="none" stroke="#fff" stroke-width="2.5"><rect x="3" y="8" width="20" height="14" rx="2"/><path d="M23 12h7l5 6v4H23z"/><circle cx="10" cy="24" r="3" fill="#0b3f8c"/><circle cx="29" cy="24" r="3" fill="#0b3f8c"/></g></svg><h3>Gutter cleaning</h3></div>
      <div class="service-card"><svg viewBox="0 0 38 30"><g fill="none" stroke="#fff" stroke-width="2.5"><rect x="3" y="8" width="20" height="14" rx="2"/><path d="M23 12h7l5 6v4H23z"/><circle cx="10" cy="24" r="3" fill="#0b3f8c"/><circle cx="29" cy="24" r="3" fill="#0b3f8c"/></g></svg><h3>Fire and flood restoration capability</h3></div>
      <div class="service-card"><svg viewBox="0 0 38 30"><g fill="none" stroke="#fff" stroke-width="2.5"><rect x="3" y="8" width="20" height="14" rx="2"/><path d="M23 12h7l5 6v4H23z"/><circle cx="10" cy="24" r="3" fill="#0b3f8c"/><circle cx="29" cy="24" r="3" fill="#0b3f8c"/></g></svg><h3>End of lease cleaning - no power required</h3></div>
      <div class="service-card highlight"><svg viewBox="0 0 38 30"><g fill="none" stroke="#fff" stroke-width="2.5"><rect x="3" y="8" width="20" height="14" rx="2"/><path d="M23 12h7l5 6v4H23z"/><circle cx="10" cy="24" r="3" fill="#053478"/><circle cx="29" cy="24" r="3" fill="#053478"/></g></svg><h3>Commercial and residential carpet/upholstery cleaning</h3></div>
      <div class="service-card"><svg viewBox="0 0 38 30"><g fill="none" stroke="#fff" stroke-width="2.5"><rect x="3" y="8" width="20" height="14" rx="2"/><path d="M23 12h7l5 6v4H23z"/><circle cx="10" cy="24" r="3" fill="#0b3f8c"/><circle cx="29" cy="24" r="3" fill="#0b3f8c"/></g></svg><h3>Whole house package solutions</h3><p>available to include gutter, tiles, carpets, upholstery, driveways and external walls etc.</p></div>
      <div class="service-card"><svg viewBox="0 0 38 30"><g fill="none" stroke="#fff" stroke-width="2.5"><rect x="3" y="8" width="20" height="14" rx="2"/><path d="M23 12h7l5 6v4H23z"/><circle cx="10" cy="24" r="3" fill="#0b3f8c"/><circle cx="29" cy="24" r="3" fill="#0b3f8c"/></g></svg><h3>Graffiti removal to a lesser extent</h3></div>
      <div class="service-card"><svg viewBox="0 0 38 30"><g fill="none" stroke="#fff" stroke-width="2.5"><rect x="3" y="8" width="20" height="14" rx="2"/><path d="M23 12h7l5 6v4H23z"/><circle cx="10" cy="24" r="3" fill="#0b3f8c"/><circle cx="29" cy="24" r="3" fill="#0b3f8c"/></g></svg><h3>NCRA Accredited Technicians</h3></div>
    </div>
  </section>

  <section class="clients">
    <h2>OUR CLIENTS</h2>
    <div class="client-row">
      <div class="client-box">K&amp;T Holdings</div>
      <div class="client-box">K&amp;T Holdings</div>
      <div class="client-box">K&amp;T Holdings</div>
      <div class="client-box">K&amp;T Holdings</div>
    </div>
  </section>

  <section class="contact">
    <h2>CONTACT US</h2>
    <div class="contact-form">
      <div class="field-pair"><div class="field">Your Name</div><div class="field">Your Email</div></div>
      <div class="field">Subject</div>
      <div class="field message">Message</div>
      <div class="send">Send Message</div>
    </div>
    <div class="contact-info">
      <div class="info-line"><svg viewBox="0 0 16 16"><path d="M8 1a5 5 0 0 0-5 5c0 4 5 9 5 9s5-5 5-9a5 5 0 0 0-5-5z" fill="none" stroke="#9fb6e6" stroke-width="1.5"/><circle cx="8" cy="6" r="1.8" fill="#9fb6e6"/></svg><span>Director Martin Halloway K&amp;T HOLDINGS CLEANING SERVICES PTY LTD 27 Wren Close Ashgrove Park 3051</span></div>
      <div class="info-line"><svg viewBox="0 0 16 16"><path d="M3 2l3 0 1.5 3.5-2 1.2a8 8 0 0 0 3.8 3.8l1.2-2L14 10v3a1 1 0 0 1-1 1A11 11 0 0 1 2 3a1 1 0 0 1 1-1z" fill="none" stroke="#9fb6e6" stroke-width="1.4"/></svg><span>+1 5550 10234 77</span></div>
      <div class="info-line"><svg viewBox="0 0 16 16"><path d="M3 2l3 0 1.5 3.5-2 1.2a8 8 0 0 0 3.8 3.8l1.2-2L14 10v3a1 1 0 0 1-1 1A11 11 0 0 1 2 3a1 1 0 0 1 1-1z" fill="none" stroke="#9fb6e6" stroke-width="1.4"/></svg><span>22 555 018 042</span></div>
    </div>
    <div class="map" role="img" aria-label="Street map showing the business location"></div>
  </section>

  <footer class="site-footer">© Copyright 2019 <b>K&amp;T Holdings Cleaners.</b> All Rights Reserved</footer>
</div>
</body>
</html>
```